Landing Page Design

We need a landing page template designed to support a clients Zenfy Bidpost Campaigns. The client is called Morlet Plumbing and they install and repair hot water systems (only). They provide no other plumbing services.

We are really looking for a great looking landing page that is both engaging and functional.

Target Market(s)

Residential/Domestic market. Typically wives and partners who are typically home or run the household.

Industry/Entity Type

Plumbing

Number of Pages Required

1 page

Requirements
Must have
• Strong branding
Strong call to actions
Great and obvious looking buttons
Nice to have
• Smart use of colour
Should not have
• The design should not use old-style, serif fonts.

Do not include any plumbing images

```html
<!DOCTYPE html>
<html lang="en">
<head>
<meta charset="utf-8">
<title>Morlet Plumbing – Hot Water Now</title>
<link rel="stylesheet" href="https://fonts.googleapis.com/css2?family=Arimo:ital,wght@0,400;0,700;1,700&display=swap">
<style>
  :root {
    --orange: #f47a35;
    --orange-light: #fba54a;
    --orange-dark: #ef7336;
    --green: #5bb75a;
    --green-light: #7cc874;
    --green-dark: #46a043;
    --brand-red: #e2232a;
    --text-grey: #666666;
    --heading-grey: #606060;
    --rule: #dddddd;
    --white: #ffffff;
    --button-grey: #d6d6d6;
    --button-grey-text: #606060;
  }
  * { box-sizing: border-box; margin: 0; padding: 0; }
  html, body { width: 983px; height: 1200px; overflow: hidden; background: var(--white); }
  body { font-family: "Arimo", Arial, sans-serif; color: var(--text-grey); }
  .page { position: relative; width: 950px; height: 1160px; transform: scale(1.0347); transform-origin: 0 0; }
  .abs { position: absolute; }

  .brand { left: 18px; top: 52px; display: flex; align-items: center; gap: 10px; }
  .brand-mark { width: 34px; height: 34px; border-radius: 50%; background: var(--orange); }
  .brand-name { font-size: 30px; font-weight: 700; color: var(--brand-red); letter-spacing: -0.5px; }

  .header-call { right: 15px; top: 72px; font-size: 24px; color: var(--orange); }
  .header-call em { font-weight: 700; }
  .header-call strong { font-size: 34px; font-weight: 400; }

  .hero { left: 12px; top: 158px; width: 597px; height: 212px;
    background: linear-gradient(90deg, var(--orange-light), var(--orange) 100%);
    color: var(--white); text-align: center; overflow: hidden; }
  .hero-title { margin-top: 34px; font-size: 67px; font-weight: 700; font-style: italic; text-shadow: 0 2px 3px rgba(0,0,0,.25); }
  .hero-sub { margin-top: 6px; font-size: 46px; font-weight: 700; text-shadow: 0 2px 3px rgba(0,0,0,.25); }

  .panel { background: linear-gradient(180deg, var(--green-light), var(--green) 45%, var(--green-dark));
    border-radius: 4px; color: var(--white); box-shadow: 0 1px 2px rgba(0,0,0,.2); }
  .features { left: 624px; top: 158px; width: 311px; height: 249px; padding: 22px 0 0 28px; list-style: none; }
  .features li { display: flex; align-items: center; gap: 10px; height: 44px; font-size: 18px; font-weight: 700; text-shadow: 0 1px 2px rgba(0,0,0,.3); }
  .tick { width: 32px; height: 30px; flex: none; }

  .section-title { left: 19px; top: 398px; font-size: 28px; color: var(--heading-grey); }
  .section-rule { left: 19px; top: 433px; width: 590px; height: 1px; background: var(--rule); }
  .copy { left: 19px; top: 446px; width: 360px; font-size: 16.5px; line-height: 21.5px; }
  .copy p + p { margin-top: 21.5px; }

  .photo-frame { left: 409px; top: 449px; width: 200px; height: 329px; background: var(--white);
    box-shadow: 0 1px 4px rgba(0,0,0,.3); padding: 9px; }
  .photo { width: 100%; height: 100%; background: linear-gradient(160deg, #3a3a3a, #9a9a9a 45%, #d9d0c8 80%, #eeeeee); }

  .btn { display: flex; align-items: center; justify-content: center; text-align: center;
    border-radius: 3px; font-weight: 700; text-transform: uppercase; text-decoration: none; box-shadow: 0 1px 2px rgba(0,0,0,.25); }
  .btn-quote { left: 82px; top: 919px; width: 186px; height: 88px; font-size: 17px; line-height: 22px; color: var(--white);
    background: linear-gradient(180deg, var(--orange-light), var(--orange-dark)); text-shadow: 0 1px 2px rgba(0,0,0,.3); }
  .btn-site { left: 331px; top: 919px; width: 186px; height: 88px; font-size: 17px; line-height: 22px; color: var(--white);
    background: linear-gradient(180deg, var(--green-light), var(--green-dark)); text-shadow: 0 1px 2px rgba(0,0,0,.3); }
  .btn-rebates { left: 82px; top: 1056px; width: 435px; height: 68px; font-size: 17px; color: var(--button-grey-text);
    background: linear-gradient(180deg, #f2f2f2, var(--button-grey)); }

  .enquiry { left: 624px; top: 428px; width: 311px; height: 695px; padding: 28px 34px 0; text-align: center; }
  .enquiry-lead { font-size: 15px; font-weight: 700; }
  .enquiry-contact { margin-top: 4px; font-size: 23px; font-weight: 700; }
  .enquiry-phone { font-size: 34px; font-weight: 700; line-height: 40px; }
  .enquiry-or { font-size: 15px; font-weight: 700; line-height: 16px; }
  .enquiry-note { font-size: 15px; font-weight: 700; margin-top: 2px; }
  .form { margin-top: 46px; text-align: left; }
  .field { display: block; margin-bottom: 10px; font-size: 13px; font-weight: 700; }
  .field span { display: block; margin-bottom: 4px; }
  .field input, .field textarea { display: block; width: 242px; height: 24px; border: 1px solid #8a8a8a; background: var(--white); }
  .field textarea { height: 110px; resize: none; }
  .btn-enquire { margin-top: 18px; width: 244px; height: 46px; font-size: 17px; color: var(--white); border: 0;
    background: linear-gradient(180deg, var(--orange-light), var(--orange-dark)); font-family: inherit; text-shadow: 0 1px 2px rgba(0,0,0,.3); }
</style>
</head>
<body>
<div class="page">
  <div class="brand abs">
    <span class="brand-mark"></span>
    <span class="brand-name">Morlet Plumbing</span>
  </div>
  <div class="header-call abs">Call <em>NOW</em> on <strong>9417 3052</strong></div>

  <div class="hero abs">
    <div class="hero-title">Hot water now!</div>
    <div class="hero-sub">SAVE $$$</div>
  </div>

  <ul class="features panel abs">
    <li><svg class="tick" viewBox="0 0 32 30"><rect x="1" y="6" width="22" height="22" fill="#fff" stroke="#ddd"/><path d="M5 16l6 7L30 2" fill="none" stroke="#fff" stroke-width="5"/><path d="M5 16l6 7L30 2" fill="none" stroke="#4a9e47" stroke-width="2"/></svg>Sydney 24 Hours 7 Days</li>
    <li><svg class="tick" viewBox="0 0 32 30"><rect x="1" y="6" width="22" height="22" fill="#fff" stroke="#ddd"/><path d="M5 16l6 7L30 2" fill="none" stroke="#fff" stroke-width="5"/><path d="M5 16l6 7L30 2" fill="none" stroke="#4a9e47" stroke-width="2"/></svg>On Time</li>
    <li><svg class="tick" viewBox="0 0 32 30"><rect x="1" y="6" width="22" height="22" fill="#fff" stroke="#ddd"/><path d="M5 16l6 7L30 2" fill="none" stroke="#fff" stroke-width="5"/><path d="M5 16l6 7L30 2" fill="none" stroke="#4a9e47" stroke-width="2"/></svg>Professional Technicians</li>
    <li><svg class="tick" viewBox="0 0 32 30"><rect x="1" y="6" width="22" height="22" fill="#fff" stroke="#ddd"/><path d="M5 16l6 7L30 2" fill="none" stroke="#fff" stroke-width="5"/><path d="M5 16l6 7L30 2" fill="none" stroke="#4a9e47" stroke-width="2"/></svg>We Advise on Rebates</li>
    <li><svg class="tick" viewBox="0 0 32 30"><rect x="1" y="6" width="22" height="22" fill="#fff" stroke="#ddd"/><path d="M5 16l6 7L30 2" fill="none" stroke="#fff" stroke-width="5"/><path d="M5 16l6 7L30 2" fill="none" stroke="#4a9e47" stroke-width="2"/></svg>Authorised Velmar Dealer</li>
  </ul>

  <h2 class="section-title abs">Solar Hot Water Systems</h2>
  <div class="section-rule abs"></div>
  <div class="copy abs">
    <p>Engage our routine office cleaning for at least 6 months and receive a FREE Carpet and Window clean! No strings attached, no contracts.</p>
    <p>To take advantage of this great offer call us on 1300 58 71 40 or complete and submit the form on this page.</p>
    <p>At Talvoro we provide all your property service needs -- painlessly. We understand that cleaning and other property services should be background activities. A set and forget proposition.</p>
  </div>

  <div class="photo-frame abs">
    <div class="photo" role="img" aria-label="Lifestyle photo of a person enjoying a warm shower"></div>
  </div>

  <a class="btn btn-quote abs" href="#">Book a<br>free quote</a>
  <a class="btn btn-site abs" href="#">Visit our<br>website</a>
  <a class="btn btn-rebates abs" href="#">Click here for information on rebates</a>

  <div class="enquiry panel abs">
    <div class="enquiry-lead">Take advantage of this great offer.</div>
    <div class="enquiry-contact">Contact Us NOW on</div>
    <div class="enquiry-phone">9417 3052</div>
    <div class="enquiry-or">or</div>
    <div class="enquiry-note">register your interest below.</div>
    <form class="form">
      <label class="field"><span>Your First Name:</span><input type="text"></label>
      <label class="field"><span>Your Surname:</span><input type="text"></label>
      <label class="field"><span>Your Suburb:</span><input type="text"></label>
      <label class="field"><span>Best Contact Number:</span><input type="text"></label>
      <label class="field"><span>Your Email Address:</span><input type="text"></label>
      <label class="field"><span>Enquiry / Comments:</span><textarea></textarea></label>
      <button class="btn btn-enquire" type="button">Enquire now</button>
    </form>
  </div>
</div>
</body>
</html>
```